TORV graphic design elements

TORV is a group of schools who have adopted positive psychology as the framework for their wellbeing programs.

Designs should be simple and formal (rather than ultra modern/trendy)

I require quotes for the following:
Letterhead
Business Card
Powerpoint slides
Pull up banner (approx 2m high)
Colour pallette development

I have uploaded a copy of our logo

```html
<!DOCTYPE html>
<html lang="en">
<head>
<meta charset="utf-8">
<title>TORV Business Card</title>
<link rel="stylesheet" href="https://fonts.googleapis.com/css2?family=Open+Sans:wght@400;600;700&display=swap">
<style>
  :root {
    --orange: #f5901e;
    --white: #ffffff;
    --backdrop: #e9e9e9;
    --card-shadow: rgba(0, 0, 0, 0.18);
  }
  * { margin: 0; padding: 0; box-sizing: border-box; }
  html, body {
    width: 1200px;
    height: 1000px;
    overflow: hidden;
    background: var(--backdrop);
    font-family: "Open Sans", sans-serif;
  }
  .business-card {
    position: absolute;
    left: 110px;
    top: 215px;
    width: 980px;
    height: 571px;
    background: var(--white);
    box-shadow: 0 6px 24px var(--card-shadow);
    overflow: hidden;
  }
  .brand {
    position: absolute;
    left: 52px;
    top: 82px;
    display: flex;
    align-items: center;
    gap: 22px;
  }
  .brand-dot {
    width: 72px;
    height: 72px;
    border-radius: 50%;
    background: var(--orange);
  }
  .brand-name {
    font-size: 104px;
    font-weight: 700;
    line-height: 1;
    color: var(--orange);
    letter-spacing: 2px;
  }
  .phone-band {
    position: absolute;
    left: 520px;
    top: 80px;
    right: 0;
    height: 124px;
    background: var(--orange);
    display: flex;
    align-items: center;
    padding-left: 34px;
  }
  .phone-number {
    color: var(--white);
    font-size: 34px;
    font-weight: 400;
  }
  .contact {
    position: absolute;
    left: 67px;
    top: 318px;
    color: var(--orange);
  }
  .contact-name {
    font-size: 30px;
    font-weight: 700;
    letter-spacing: 3px;
    margin-bottom: 20px;
  }
  .contact-address {
    font-size: 29px;
    font-weight: 400;
    line-height: 1.3;
  }
  .footer-band {
    position: absolute;
    left: 0;
    right: 0;
    bottom: 0;
    height: 62px;
    background: var(--orange);
  }
</style>
</head>
<body>
  <div class="business-card">
    <div class="brand">
      <span class="brand-dot"></span>
      <span class="brand-name">TORV</span>
    </div>
    <div class="phone-band">
      <span class="phone-number">ph. 0834.562.190</span>
    </div>
    <div class="contact">
      <p class="contact-name">Daniel Marsh ,S PD</p>
      <p class="contact-address">Linden Street No. 14<br>North of Kartika, West Java 40217</p>
    </div>
    <div class="footer-band"></div>
  </div>
</body>
</html>
```